Nordisk Husforum

Company is in: Denmark - Copenhagen
It sells: Restaurants and café buildings
Companys age: 25 years
Main benefit: trust with over 25 years experience

```html
<!DOCTYPE html>
<html lang="en">
<head>
<meta charset="utf-8">
<title>Nordisk Husforum</title>
<link rel="stylesheet" href="https://fonts.googleapis.com/css2?family=EB+Garamond:wght@400&family=Open+Sans:wght@400;600&family=Arimo:wght@400;700&display=swap">
<style>
:root{
  --page:#2d2d2d;
  --header-top:#1e1e1e;
  --header-bottom:#111;
  --nav:#262626;
  --panel:#212121;
  --tab:#151515;
  --accent:#f5a812;
  --text:#e8e8e8;
  --muted:#bdbdbd;
  --line:#3c3c3c;
  --frame:#d8d8d8;
  --field:#2a2a2a;
}
*{margin:0;padding:0;box-sizing:border-box}
html,body{width:1120px;height:1200px;overflow:hidden}
body{background:var(--page);font-family:"Arimo",Arial,sans-serif;color:var(--text);position:relative}
.abs{position:absolute}

/* header */
.site-header{left:0;top:0;width:1120px;height:129px;background:linear-gradient(180deg,#2a2a2a,var(--header-bottom));border-bottom:1px solid #444}
.brand{left:47px;top:42px;font-family:"EB Garamond",Georgia,serif;font-size:41px;color:#fff;letter-spacing:.3px}
.login-field{top:38px;width:164px;height:33px;border:1px solid #666;border-radius:6px;background:var(--field);font-family:"Open Sans",sans-serif;font-size:14px;color:#bbb;padding:6px 9px}
.forgot{left:829px;top:94px;font-size:12px;color:var(--accent);font-family:"Open Sans",sans-serif}
.login-btn{left:983px;top:89px;width:72px;height:24px;border:1px solid #777;border-radius:6px;background:linear-gradient(#555,#2a2a2a);font-family:"Open Sans",sans-serif;font-size:13px;color:#fff;display:flex;align-items:center;justify-content:center;gap:5px}

/* navigation */
.main-nav{left:0;top:130px;width:1120px;height:54px;background:linear-gradient(#333,var(--nav));border-bottom:1px solid #111}
.nav-item{top:0;height:54px;line-height:54px;font-family:"Open Sans",sans-serif;font-size:14px;color:#ddd}
.nav-sep{top:12px;width:1px;height:30px;background:#444;border-right:1px solid #1a1a1a}
.nav-home{left:45px;top:10px;width:74px;height:32px;border:1px solid #666;border-radius:6px;background:linear-gradient(#1a1a1a,#333);color:#fff;font-weight:600;font-size:14px;font-family:"Open Sans",sans-serif;text-align:center;line-height:30px}
.search{left:885px;top:14px;width:198px;height:25px;background:#f2f2f2;border:1px solid #999}

/* slider */
.slider-frame{left:37px;top:207px;width:1054px;height:371px;background:var(--frame);box-shadow:0 14px 16px -8px #000}
.slider-photo{left:13px;top:10px;width:1029px;height:350px;background:linear-gradient(180deg,#6c88b8 0%,#a6b5cc 35%,#d59462 55%,#8a5a36 72%,#3a2e2a 100%)}
.slider-bar{left:0;bottom:0;width:100%;height:40px;background:rgba(20,20,20,.85)}
.dot{top:14px;width:13px;height:13px;border-radius:50%;background:#fff}
.dot.active{background:transparent;border:2px solid var(--accent);width:18px;height:18px;top:11px}
.arrow-btn{top:12px;width:19px;height:19px;background:#ddd;border:1px solid #888}

/* content panel */
.content-panel{left:35px;top:610px;width:1056px;height:464px;background:var(--panel);border-radius:4px}
.tab-title{height:37px;background:linear-gradient(#3a3a3a,var(--tab));border-radius:4px 4px 0 0;font-family:"Open Sans",sans-serif;font-size:24px;color:#fff;padding-left:18px;line-height:36px}
.tab-title .hl{color:var(--accent)}
.intro{left:23px;top:60px;width:760px;font-size:13px;line-height:22.5px;color:#e6e6e6;letter-spacing:.2px}
.intro p{margin-bottom:10px}
.intro strong{font-weight:700;color:#fff}
.see-more{left:697px;top:240px;font-size:13px;color:#eee;letter-spacing:.5px}
.card-title{top:283px;font-family:"Open Sans",sans-serif;font-size:19px;color:#eee}
.card-photo{top:314px;width:213px;height:130px;border:2px solid #555}
.divider{left:790px;top:-35px;width:1px;height:388px;background:var(--line)}
.map{left:820px;top:66px;width:196px;height:145px;background:linear-gradient(135deg,#e9d96c,#f3e79a 50%,#9cc66d)}
.find-us{left:948px;top:222px;font-size:13px;color:#eee;letter-spacing:.4px}
.touch{left:812px;top:285px;font-family:"Open Sans",sans-serif;font-size:22px;color:#eee;display:flex;align-items:center;gap:10px}
.social{left:812px;width:214px;height:38px;border:1px solid #444;border-radius:6px;background:linear-gradient(#2b2b2b,#161616);font-family:"Open Sans",sans-serif;font-size:14.5px;color:#fff;display:flex;align-items:center;gap:10px;padding-left:4px}
.social-mark{width:30px;height:30px;border-radius:4px;background:#4a6aa8}

/* footer */
.site-footer{left:0;top:1119px;width:1120px;height:81px;background:linear-gradient(#262626,#181818);border-top:1px solid #444}
.footer-links{left:0;top:14px;width:1120px;text-align:center;font-size:13px;color:#fff;letter-spacing:.3px;word-spacing:2px}
.footer-links span{margin:0 17px}
.copyright{left:0;top:44px;width:1120px;text-align:center;font-size:13px;color:#fff;letter-spacing:.3px}
</style>
</head>
<body>

<header class="site-header abs">
  <div class="brand abs">Nordisk Husforum</div>
  <div class="login-field abs" style="left:726px">Bruger</div>
  <div class="login-field abs" style="left:910px">Kodeord</div>
  <div class="forgot abs">Forgot your Password ?</div>
  <div class="login-btn abs">
    <svg width="10" height="12" viewBox="0 0 10 12" aria-hidden="true"><rect x="1" y="5" width="8" height="7" rx="1" fill="#ddd"/><path d="M3 5V3a2 2 0 0 1 4 0v2" stroke="#ddd" stroke-width="1.5" fill="none"/></svg>Login
  </div>
</header>

<nav class="main-nav abs">
  <div class="nav-home abs">Home</div>
  <div class="nav-sep abs" style="left:133px"></div>
  <div class="nav-item abs" style="left:161px">Company Info</div>
  <div class="nav-sep abs" style="left:283px"></div>
  <div class="nav-item abs" style="left:313px">Sales List</div>
  <div class="nav-sep abs" style="left:404px"></div>
  <div class="nav-item abs" style="left:433px">Links / Download</div>
  <div class="nav-sep abs" style="left:579px"></div>
  <div class="nav-item abs" style="left:607px">Newsletter</div>
  <div class="nav-sep abs" style="left:712px"></div>
  <div class="nav-item abs" style="left:738px">Contact Us</div>
  <div class="search abs">
    <svg class="abs" style="right:4px;top:3px" width="18" height="18" viewBox="0 0 18 18" aria-hidden="true"><circle cx="7" cy="7" r="5" stroke="#111" stroke-width="2" fill="none"/><path d="M11 11l5 5" stroke="#111" stroke-width="2.5"/></svg>
  </div>
</nav>

<section class="slider-frame abs">
  <div class="slider-photo abs" role="img" aria-label="City skyline with office towers at sunset">
    <div class="slider-bar abs">
      <div class="dot abs" style="left:434px"></div>
      <div class="dot active abs" style="left:456px"></div>
      <div class="dot abs" style="left:482px"></div>
      <div class="dot abs" style="left:507px"></div>
      <div class="dot abs" style="left:533px"></div>
      <div class="arrow-btn abs" style="left:969px"><svg width="17" height="17" viewBox="0 0 17 17" aria-hidden="true"><path d="M10 4l-4 4.5 4 4.5" stroke="#333" stroke-width="1.6" fill="none"/></svg></div>
      <div class="arrow-btn abs" style="left:991px"><svg width="17" height="17" viewBox="0 0 17 17" aria-hidden="true"><path d="M7 4l4 4.5-4 4.5" stroke="#333" stroke-width="1.6" fill="none"/></svg></div>
    </div>
  </div>
</section>

<main class="content-panel abs">
  <h1 class="tab-title abs" style="left:21px;top:16px;width:449px;font-weight:400">Welcome to <span class="hl">Nordisk Husforum</span></h1>
  <div class="intro abs">
    <p><strong>NORDISK HUSFORUM</strong> has over 25 years experience in the industry, it has given us a thorough knowledge of the industry's many subtleties and we can therefore say with certainty that you will be in good hands with whether you want to sell or industry,</p>
    <p>Subtleties and we can therefore say with certainty that you will be in good handsa thorough knowledge of the industry's many subtleties and we can therefore say with certainty that you will be in good hands with whether you want to knowledge of the industry's many subtleties and we can therefore say with certainty that you will be in good hands with&nbsp; whether you want to sell or buya catering company.</p>
  </div>
  <div class="see-more abs">see more..</div>

  <div class="card-title abs" style="left:47px">Ugens Forretning</div>
  <div class="card-photo abs" style="left:38px;background:linear-gradient(120deg,#4f93e0 0%,#8cc0f0 55%,#b8bec8 60%,#7d8796 100%)" role="img" aria-label="Glass office building against blue sky"></div>
  <div class="card-title abs" style="left:289px">Sog Forretninger</div>
  <div class="card-photo abs" style="left:285px;background:linear-gradient(90deg,#cfcfcf,#f4f4f4 40%,#9a9a9a 70%,#e8e8e8)" role="img" aria-label="White spiral building facade"></div>
  <div class="card-title abs" style="left:536px">Building Forretning</div>
  <div class="card-photo abs" style="left:532px;background:linear-gradient(110deg,#1c4fa8,#3a86e0 50%,#0f3f9a)" role="img" aria-label="Blue glass tower facade"></div>

  <div class="divider abs" style="top:40px"></div>

  <h2 class="tab-title abs" style="left:818px;top:16px;width:193px;font-weight:400;font-size:21px;padding-left:13px">Location map
    <svg class="abs" style="right:12px;top:10px" width="22" height="24" viewBox="0 0 22 24" aria-hidden="true"><path d="M3 4h11v10" stroke="var(--accent)" stroke-width="4" fill="none"/><path d="M8 13h12l-6 8z" fill="var(--accent)"/></svg>
  </h2>
  <div class="map abs" role="img" aria-label="Street map of central Copenhagen with office location"></div>
  <div class="find-us abs">Find us &gt;&gt;</div>

  <div class="touch abs">
    <svg width="36" height="34" viewBox="0 0 36 34" aria-hidden="true"><rect x="2" y="6" width="24" height="26" rx="2" fill="#dfe8f0"/><path d="M6 14h16M6 19h16M6 24h12" stroke="#7a9ab8" stroke-width="1.5"/><path d="M16 24l16-18 3 3-16 18-5 2z" fill="#4a8fd0"/></svg>
    Get in touch
  </div>
  <div class="social abs" style="top:328px"><span class="social-mark"></span>Follow us Circlebook</div>
  <div class="social abs" style="top:371px"><span class="social-mark" style="background:#5aaee0"></span>Follow us Chirpline</div>
  <div class="social abs" style="top:415px"><span class="social-mark" style="background:#e6e6e6"></span>Follow us Callwave</div>
</main>

<footer class="site-footer abs">
  <div class="footer-links abs">Home<span>|</span>Company Info<span>|</span>Sales List<span>|</span>Links / Download<span>|</span>Newsletter<span>|</span>Contact Us</div>
  <div class="copyright abs">Copyright © 2011 Nordisk Husforum. All right reserved</div>
</footer>

</body>
</html>
```